Website with links and a professional business card

Bridging the Financial Gap is our Mission statement or MOTO
Please use my LOGO that was created by Pixel harbor.
We offer Tax & Accounting
We provide Tax Planning
Retirement planning
New business start ups
Payroll
Business Advice and planning
We strive to excellence and convey a family friendly Tax Firm. We offer QVO links to learn more.

Target Market(s)

Tax & Accouting

Industry/Entity Type

Tax & Accounting

Contact Information for Business Card

Classy and elegant for a Women owned Business

Colors

Designer to choose colors to be used in the design.

Requirements
Must have
• Logo, Owners Name, Phone numbers QR code to the website
Nice to have
• My logo center on the card with nice colors that enhance the Silver, Navy blue and red
Should not have
• No currency signs or symbols

```html
<!DOCTYPE html>
<html lang="en">
<head>
<meta charset="utf-8">
<title>Span Partners – Business Card</title>
<link href="https://fonts.googleapis.com/css2?family=Montserrat:wght@400;500;800&display=swap" rel="stylesheet">
<style>
  :root {
    --stage: #d4d4d1;
    --paper: #ffffff;
    --navy: #0d1a3f;
    --silver: #7d7d7f;
    --red: #c8202b;
    --ink: #2a2a2a;
  }
  * { margin: 0; padding: 0; box-sizing: border-box; }
  html, body {
    width: 1200px;
    height: 801px;
    overflow: hidden;
  }
  body {
    background: var(--stage);
    font-family: "Montserrat", sans-serif;
    position: relative;
  }
  .card {
    position: absolute;
    top: 245px;
    width: 540px;
    height: 310px;
    background: var(--paper);
    border-bottom: 3px solid var(--red);
    border-left: 3px solid var(--red);
    box-shadow: 0 10px 24px rgba(0,0,0,0.18);
  }
  .card--contact { left: 40px; }
  .card--brand { left: 620px; }

  .card__tab {
    position: absolute;
    top: 0;
    right: 0;
    width: 12px;
    height: 40px;
    background: var(--red);
  }
  .holder {
    position: absolute;
    top: 34px;
    right: 34px;
    text-align: right;
  }
  .holder__name {
    font-weight: 800;
    font-size: 21px;
    color: var(--navy);
    letter-spacing: 0.5px;
  }
  .holder__role {
    font-weight: 400;
    font-size: 13px;
    color: var(--ink);
    margin-top: 2px;
  }
  .brand-name {
    font-weight: 800;
    color: var(--navy);
    text-transform: uppercase;
    letter-spacing: 2px;
    white-space: nowrap;
  }
  .card--contact .brand-name {
    position: absolute;
    left: 30px;
    top: 128px;
    font-size: 26px;
  }
  .contact {
    position: absolute;
    left: 30px;
    bottom: 26px;
    font-size: 12.5px;
    color: var(--ink);
    line-height: 1.45;
  }
  .contact__address { margin-bottom: 12px; }
  .contact__line {
    display: flex;
    align-items: center;
    gap: 7px;
  }
  .contact__icon { width: 12px; height: 12px; flex: none; }

  .card--brand .brand-name {
    position: absolute;
    left: 0;
    right: 0;
    top: 50%;
    transform: translateY(-50%);
    text-align: center;
    font-size: 46px;
  }
</style>
</head>
<body>
  <section class="card card--contact">
    <div class="card__tab"></div>
    <div class="holder">
      <p class="holder__name">NORA WHITFIELD</p>
      <p class="holder__role">Managing Director</p>
    </div>
    <p class="brand-name">Span Partners</p>
    <div class="contact">
      <p class="contact__address">Your address, City<br>State, Zip 1234</p>
      <p class="contact__line">
        <svg class="contact__icon" viewBox="0 0 12 12" aria-hidden="true"><path d="M2.5 1 L4.5 1 L5.3 3.5 L4 4.5 Q5 7 7.5 8 L8.5 6.7 L11 7.5 L11 9.5 Q10.5 11 9 11 Q1 10 1 3 Q1 1.5 2.5 1 Z" fill="var(--red)"/></svg>
        123 456 789
      </p>
      <p class="contact__line">
        <svg class="contact__icon" viewBox="0 0 12 12" aria-hidden="true"><rect x="0.5" y="2" width="11" height="8" rx="1" fill="var(--red)"/><path d="M1 2.5 L6 6.5 L11 2.5" stroke="#fff" stroke-width="1" fill="none"/></svg>
        info@yourgmail.com
      </p>
      <p class="contact__line">
        <svg class="contact__icon" viewBox="0 0 12 12" aria-hidden="true"><circle cx="6" cy="6" r="5.5" fill="var(--red)"/><path d="M0.5 6 H11.5 M6 0.5 Q3 6 6 11.5 M6 0.5 Q9 6 6 11.5" stroke="#fff" stroke-width="0.8" fill="none"/></svg>
        www.yourwebsite.com
      </p>
    </div>
  </section>

  <section class="card card--brand">
    <p class="brand-name">Span Partners</p>
  </section>
</body>
</html>
```